Brennock Holdings LLC, new Business cards

I'm moving offices and need new cards. Plus I'm open to modifying the current design of my card. I will keep the logo but would like to explore other layouts and fonts for the design. I've included the current double sided card for reference. I Like the navy color and white. Might be open to grays or silver. Needs to be clean and elegant.

Target Market(s)

Investors, buyers & sellers of private equities and real estate.

Contact Information for Business Card

Brennock Holdings
Desmond K.R. Whitfield, Managing Principal
418 Harwick Ave., Suite 310
Denver, CO 80299
M: 970-555-0147, O: 303-555-0193
Desmond@brennockholdings.example
Brennockholdings.example

Colors
0354a2
ffffff
c4c4c4

Requirements
Must have
• Business card details.
• Logo raised or embossed, it was designed after a wax seal. Current has raised ink.
Nice to have
• Space on card to write additional notes.

```html
<!DOCTYPE html>
<html lang="en">
<head>
<meta charset="utf-8">
<title>Brennock Holdings – Business Cards</title>
<link href="https://fonts.googleapis.com/css2?family=PT+Sans:wght@400;700&display=swap" rel="stylesheet">
<style>
  :root {
    --navy: #2d2a6c;
    --ink: #4a4a4f;
    --paper: #fbfbfa;
    --edge: #e4e2dc;
    --ground: #ece9e4;
  }
  * { margin: 0; padding: 0; box-sizing: border-box; }
  html, body { width: 1200px; height: 800px; overflow: hidden; }
  body {
    background: var(--ground);
    font-family: "PT Sans", Arial, sans-serif;
    display: flex;
    align-items: center;
    justify-content: center;
    gap: 48px;
  }
  .card {
    position: relative;
    width: 540px;
    height: 309px;
    background: var(--paper);
    border: 1px solid var(--edge);
    box-shadow: 0 2px 6px rgba(0,0,0,0.08);
  }

  /* Front */
  .front-brand {
    position: absolute;
    left: 40px;
    top: 96px;
    width: 200px;
    display: flex;
    align-items: center;
    gap: 12px;
  }
  .brand-dot {
    flex: none;
    width: 34px;
    height: 34px;
    border-radius: 50%;
    background: var(--navy);
  }
  .brand-name {
    color: var(--navy);
    font-weight: 700;
    font-size: 22px;
    line-height: 1.1;
    letter-spacing: 0.04em;
    text-transform: uppercase;
  }
  .details {
    position: absolute;
    left: 262px;
    top: 84px;
    color: var(--ink);
    font-size: 14px;
    line-height: 1.3;
  }
  .person-name {
    color: var(--navy);
    font-weight: 700;
    font-size: 20px;
    line-height: 1.1;
  }
  .person-title { margin-bottom: 8px; }
  .address { margin-bottom: 6px; }
  .contact-row {
    display: flex;
    align-items: center;
    gap: 7px;
  }
  .contact-row svg { width: 12px; height: 12px; flex: none; fill: var(--ink); }
  .contact-row.web { padding-left: 19px; }

  /* Back */
  .back-brand {
    position: absolute;
    right: 40px;
    bottom: 70px;
    display: flex;
    align-items: center;
    gap: 8px;
  }
  .back-brand .brand-dot { width: 18px; height: 18px; }
  .back-brand .brand-name { font-size: 13px; }
  .back-web {
    position: absolute;
    right: 40px;
    bottom: 40px;
    color: var(--ink);
    font-size: 14px;
    letter-spacing: 0.14em;
  }
</style>
</head>
<body>

  <section class="card card-front" aria-label="Business card front">
    <div class="front-brand">
      <span class="brand-dot"></span>
      <span class="brand-name">Brennock Holdings</span>
    </div>
    <div class="details">
      <p class="person-name">Desmond K.R. Whitfield</p>
      <p class="person-title">CEO</p>
      <p class="address">418 Harwick Ave., Suite 310<br>Denver, CO 80299</p>
      <p class="contact-row">
        <svg viewBox="0 0 12 12" aria-hidden="true"><path d="M2.4 1h2l1 2.6-1.3 1a6 6 0 0 0 2.8 2.8l1-1.3L10.5 7v2a1.4 1.4 0 0 1-1.5 1.4A8.3 8.3 0 0 1 1 2.5 1.4 1.4 0 0 1 2.4 1z"/></svg>
        303.555.0193
      </p>
      <p class="contact-row">
        <svg viewBox="0 0 12 12" aria-hidden="true"><path d="M3.5 0.5h5a1 1 0 0 1 1 1v9a1 1 0 0 1-1 1h-5a1 1 0 0 1-1-1v-9a1 1 0 0 1 1-1zM3.6 1.8v7.4h4.8V1.8zM6 9.8a.6.6 0 1 0 0 1.2.6.6 0 0 0 0-1.2z"/></svg>
        970.555.0147
      </p>
      <p class="contact-row">
        <svg viewBox="0 0 12 12" aria-hidden="true"><circle cx="6" cy="6" r="5.5"/><path d="M3 4.5h6v3.5H3z" fill="#fbfbfa"/><path d="M3 4.5l3 2 3-2" stroke="#4a4a4f" stroke-width=".8" fill="none"/></svg>
        Desmond@brennockholdings.example
      </p>
      <p class="contact-row web">Brennockholdings.example</p>
    </div>
  </section>

  <section class="card card-back" aria-label="Business card back">
    <div class="back-brand">
      <span class="brand-dot"></span>
      <span class="brand-name">Brennock Holdings</span>
    </div>
    <p class="back-web">Brennockholdings.example</p>
  </section>

</body>
</html>
```